Investment Funding, Building and Construction

I need a design logo for my new business based out of Houston, TX called Kestrel Ridge Holdings LLC., We are a company looking to help fund and invest into other small/businesses that do not want to deal with the banking system. We also remodel, renovate, and build from the ground up anything from residential, industrial warehousing, and commercial buildings. We would like the design to express our great deal of passion that we have for the work, our dedication to helping the costumer/businesses receive their expectation of work and also our professionalism and commitment to making sure we get the job done as perfect as possible. We want to build your future!

Target Market(s)

Architects, Design Companies, Home Owners and Real Estate

Industry/Entity Type

Construction Company

Contact Information for Business Card

Name: Dorian Welsby
Position: CEO/President
Company Name: Kestrel Ridge Holdings LLC.,
Website: www.kestrelridgeholds.example
Phone: 281-555-0173
Email: kestrelridgeholds@mailbox.example, crewfundline@mailbox.example

Font styles to use
Serif

Colors
f04a50
3377b5

Requirements
Must have
• Motivational, Inspiring, and Detailed oriented work but simple.
Nice to have
• I would like to see excitement and enthusiasm within the card.
Should not have
• The project can not be boring and lack of detail.

```html
<!DOCTYPE html>
<html lang="en">
<head>
<meta charset="utf-8">
<title>Kestrel Ridge Holdings LLC. — Business Card</title>
<link href="https://fonts.googleapis.com/css2?family=Source+Serif+4:opsz,wght@8..60,400;8..60,700&display=swap" rel="stylesheet">
<style>
  :root {
    --page-bg: #e8e5e1;
    --card-bg: #454547;
    --text-light: #ffffff;
    --accent-red: #f04a50;
    --accent-blue: #3377b5;
    --icon-red: #e0555d;
    --pattern-pink: #c95a78;
    --pattern-violet: #7d6a9e;
  }
  html, body {
    margin: 0;
    padding: 0;
    width: 1200px;
    height: 1006px;
    overflow: hidden;
    background: var(--page-bg);
    font-family: "Source Serif 4", Georgia, serif;
  }
  .business-card {
    position: absolute;
    left: 69px;
    top: 213px;
    width: 1050px;
    height: 600px;
    background: var(--card-bg);
    color: var(--text-light);
    overflow: hidden;
  }
  .pattern-field {
    position: absolute;
    left: 0;
    top: 0;
    width: 1050px;
    height: 600px;
  }
  .company-name {
    position: absolute;
    left: 56px;
    top: 56px;
    margin: 0;
    font-size: 38px;
    font-weight: 700;
    line-height: 1;
    white-space: nowrap;
  }
  .company-rule {
    position: absolute;
    left: 56px;
    top: 126px;
    width: 528px;
    height: 3px;
    background: linear-gradient(90deg, var(--accent-red), var(--accent-blue));
  }
  .person-name {
    position: absolute;
    left: 56px;
    top: 164px;
    margin: 0;
    font-size: 44px;
    font-weight: 400;
    line-height: 1;
  }
  .person-role {
    position: absolute;
    left: 56px;
    top: 214px;
    margin: 0;
    font-size: 32px;
    font-weight: 400;
    line-height: 1;
  }
  .contact-list {
    position: absolute;
    left: 54px;
    top: 355px;
    margin: 0;
    padding: 0;
    list-style: none;
    font-size: 28px;
    line-height: 34px;
  }
  .contact-item {
    display: flex;
    align-items: center;
    margin-bottom: 12px;
  }
  .contact-icon {
    width: 32px;
    height: 32px;
    margin-right: 30px;
    flex: none;
    fill: var(--icon-red);
  }
  .contact-text { white-space: nowrap; }
</style>
</head>
<body>
  <section class="business-card">
    <svg class="pattern-field" viewBox="0 0 1050 600" role="img" aria-label="Decorative pink and violet star-burst lattice pattern sweeping across the right side">
      <defs>
        <linearGradient id="patternTone" x1="0" y1="0" x2="1" y2="1">
          <stop offset="0" stop-color="var(--pattern-violet)"/>
          <stop offset="0.5" stop-color="var(--pattern-pink)"/>
          <stop offset="1" stop-color="var(--pattern-violet)"/>
        </linearGradient>
      </defs>
      <path d="M630 0 H1050 V600 H460 C540 520 620 470 650 410 C680 330 640 160 630 0 Z"
            fill="url(#patternTone)" opacity="0.45"/>
    </svg>

    <h1 class="company-name">Kestrel Ridge Holdings LLC.</h1>
    <div class="company-rule"></div>

    <h2 class="person-name">Dorian Welsby</h2>
    <p class="person-role">CEO/President</p>

    <ul class="contact-list">
      <li class="contact-item">
        <svg class="contact-icon" viewBox="0 0 24 24" aria-hidden="true">
          <path d="M6.6 10.8a15 15 0 0 0 6.6 6.6l2.2-2.2a1 1 0 0 1 1-.25 11.4 11.4 0 0 0 3.6.57 1 1 0 0 1 1 1V20a1 1 0 0 1-1 1A17 17 0 0 1 3 4a1 1 0 0 1 1-1h3.5a1 1 0 0 1 1 1c0 1.25.2 2.45.57 3.57a1 1 0 0 1-.25 1z"/>
        </svg>
        <span class="contact-text">281-555-0173</span>
      </li>
      <li class="contact-item">
        <svg class="contact-icon" viewBox="0 0 24 24" aria-hidden="true">
          <path d="M3 5h18a1 1 0 0 1 1 1v1.2l-10 6-10-6V6a1 1 0 0 1 1-1zM2 9.5l10 6 10-6V18a1 1 0 0 1-1 1H3a1 1 0 0 1-1-1z"/>
        </svg>
        <span class="contact-text">kestrelridgeholds@mailbox.example<br>crewfundline@mailbox.example</span>
      </li>
      <li class="contact-item">
        <svg class="contact-icon" viewBox="0 0 24 24" aria-hidden="true">
          <circle cx="12" cy="12" r="10"/>
          <path d="M7 7c2 0 3 1 3 2.5S8 11 8 13s2 2 2 4-1 2.5-1 2.5M15 5c-1 1.5 0 3 1.5 3S19 9 19 11s-2 2.5-3 3.5" fill="none" stroke="var(--card-bg)" stroke-width="1.6" stroke-linecap="round"/>
        </svg>
        <span class="contact-text">www.kestrelridgeholds.example</span>
      </li>
    </ul>
  </section>
</body>
</html>
```